Lumora Flow Collective Business Cards

I need business cards for staff in a new startup. Our company name is MorvaLeap - we train Tai Chi teachers. But our biggest project is called Lumora Flow Collective - a federal project to put together free Tai Chi classes for Vets all across America. It's a young company, with a spirit of excitement, passion, a desire to do good for others (our Vets) and a modern style and sensibility. In other words, not old-fashioned Asian martial arts theme, but something new.

Industry/Entity Type

Health And Wellness

Contact Information for Business Card

The topic is ancient healing, but the company is the Quibbletons - so I'd like a card design that captures that.

Font styles to use
Sans Serif

Colors

Designer to choose colors to be used in the design.

Requirements
Nice to have
• I've got two logos - one for the company and one for the project. I want to see if we can incorporate them both without it becoming too busy.
Should not have
• Overly old-fashioned yin-yang themes.

```html
<!DOCTYPE html>
<html lang="en">
<head>
<meta charset="UTF-8">
<title>Lumora Flow Collective Business Cards</title>
<link href="https://fonts.googleapis.com/css2?family=Montserrat:wght@400;500;600&display=swap" rel="stylesheet">
<style>
  :root {
    --stage: #2b2b2d;
    --card-black: #000000;
    --card-white: #ffffff;
    --brand-red: #d8262c;
    --brand-navy: #3b3a92;
    --text-white: #ffffff;
  }
  * { margin: 0; padding: 0; box-sizing: border-box; }
  html, body {
    width: 1200px;
    height: 900px;
    overflow: hidden;
    background: var(--stage);
    font-family: "Montserrat", sans-serif;
  }
  .stage {
    width: 1200px;
    height: 900px;
    display: flex;
    flex-direction: column;
    align-items: center;
    justify-content: center;
    gap: 40px;
  }
  .card {
    width: 700px;
    height: 386px;
    display: flex;
    box-shadow: 0 10px 28px rgba(0,0,0,0.45);
  }
  .card__side {
    width: 210px;
    background: var(--card-white);
    display: flex;
    align-items: center;
    justify-content: center;
  }
  .card__main {
    flex: 1;
    background: var(--card-black);
    display: flex;
    align-items: center;
    justify-content: center;
    position: relative;
  }
  /* company mark */
  .company-mark {
    display: flex;
    align-items: center;
    gap: 8px;
  }
  .company-mark__dot {
    width: 26px;
    height: 26px;
    border-radius: 50%;
    background: var(--brand-red);
  }
  .company-mark__name {
    font-size: 22px;
    font-weight: 600;
    color: var(--brand-red);
  }
  /* project mark */
  .project-mark {
    display: flex;
    align-items: center;
    gap: 16px;
  }
  .project-mark__ring {
    width: 84px;
    height: 84px;
    border-radius: 50%;
    border: 3px solid var(--text-white);
    flex-shrink: 0;
  }
  .project-mark__name {
    font-size: 30px;
    font-weight: 500;
    line-height: 1.1;
    color: var(--text-white);
    letter-spacing: 0.5px;
  }
  /* back side */
  .card__main--contact {
    justify-content: flex-start;
    padding-left: 40px;
    gap: 40px;
  }
  .project-mark--stacked {
    flex-direction: column;
    align-items: center;
    gap: 12px;
  }
  .project-mark--stacked .project-mark__ring {
    width: 78px;
    height: 78px;
    border-color: var(--brand-navy);
  }
  .project-mark--stacked .project-mark__name {
    font-size: 19px;
    text-align: center;
    color: var(--brand-navy);
  }
  .contact {
    display: flex;
    flex-direction: column;
  }
  .contact__name {
    font-size: 20px;
    font-weight: 500;
    letter-spacing: 1px;
    color: var(--brand-navy);
    text-transform: uppercase;
  }
  .contact__role {
    font-size: 15px;
    color: var(--brand-red);
    margin-top: 2px;
  }
  .contact__rule {
    width: 14px;
    height: 2px;
    background: var(--brand-red);
    margin: 12px 0 12px;
  }
  .contact__list { list-style: none; }
  .contact__item {
    display: flex;
    align-items: center;
    gap: 10px;
    font-size: 14px;
    color: var(--brand-navy);
    margin-bottom: 6px;
  }
  .contact__icon {
    width: 14px;
    height: 14px;
    flex-shrink: 0;
  }
</style>
</head>
<body>
<main class="stage">
  <section class="card card--front">
    <div class="card__side">
      <div class="company-mark">
        <span class="company-mark__dot"></span>
        <span class="company-mark__name">MorvaLeap</span>
      </div>
    </div>
    <div class="card__main">
      <div class="project-mark">
        <span class="project-mark__ring"></span>
        <span class="project-mark__name">Lumora Flow<br>Collective</span>
      </div>
    </div>
  </section>

  <section class="card card--back">
    <div class="card__side">
      <div class="company-mark">
        <span class="company-mark__dot"></span>
        <span class="company-mark__name">MorvaLeap</span>
      </div>
    </div>
    <div class="card__main card__main--contact">
      <div class="project-mark project-mark--stacked">
        <span class="project-mark__ring"></span>
        <span class="project-mark__name">Lumora Flow<br>Collective</span>
      </div>
      <div class="contact">
        <p class="contact__name">Arden Voss</p>
        <p class="contact__role">Founder &amp; CEO</p>
        <span class="contact__rule"></span>
        <ul class="contact__list">
          <li class="contact__item">
            <svg class="contact__icon" viewBox="0 0 16 16" fill="none" stroke="#d8262c" stroke-width="1.6" stroke-linecap="round" stroke-linejoin="round"><path d="M3 2h3l1.5 3.5-2 1.2a8 8 0 0 0 3.8 3.8l1.2-2L14 10v3a1 1 0 0 1-1 1A11 11 0 0 1 2 3a1 1 0 0 1 1-1z"/></svg>
            +00 000 555 0142
          </li>
          <li class="contact__item">
            <svg class="contact__icon" viewBox="0 0 16 16" fill="none" stroke="#d8262c" stroke-width="1.6" stroke-linejoin="round"><rect x="1.5" y="3" width="13" height="10"/><path d="M1.5 3.5 8 9l6.5-5.5"/></svg>
            hello@lumoraflow.com
          </li>
          <li class="contact__item">
            <svg class="contact__icon" viewBox="0 0 16 16" fill="none" stroke="#d8262c" stroke-width="1.5"><circle cx="8" cy="8" r="6.5"/><ellipse cx="8" cy="8" rx="2.8" ry="6.5"/><path d="M1.5 8h13"/></svg>
            www.lumoraflow.com
          </li>
        </ul>
      </div>
    </div>
  </section>
</main>
</body>
</html>
```